Toronto based adult novelty shop in need of website banners for new site

We are in need of a total of seven banners for our website.  We have one of Canada's largest selections of adult novelty items and fetish wear.  We have been serving the adult online community in Canada and the world since 2008.
There are two different sizes of banners needed.  The first measures 936px x 403px and feature products.  The other three banners measure  296px x 187px and highlight our customer policies.  The overall look we are going for should convey a sense of quality and elegance and should integrate with our new theme well.  You may view the test site by visiting http://velvetorchard.ca/testshop.  The banners displayed on the test site are placeholder graphics that came with the theme (not our banners or products).  Below is the list I've compiled for the content of the banners we need.  Product descriptions for the part numbers may be viewed by using the search box on our test website (see link above).
936 x 403 banner #1: Product number B938 Brass Tide Lubricant Copy should read something like: Brass Tide Silicone, Prepare for Action! (Military theme?)
936 x 403 banner #2: Product number AC245 Marigold Alloy Locking Anal Plug Copy should read something like: Add a new dimension to anal play
936 x 403 banner #3: Product number AB545 Leather and Brocade Nadia Corset Copy should read something like: Give your partner a visual feast
936 x 403 banner #4: Product number AD621 Orion Dusklight Premium Wand Kit Copy should read something like: Electrify your partner and light them up with this exceptional all-in-one set!
296 x 187 banner #1: Return Policy
Copy should read something like: Easy Returns, Don't like it?  Send it back! (click here for more information)
296 x 187 banner #2: Free Shipping
Copy should read something like: Free Expedited Shipping on orders over $149 (click here for details)
296 x 187 banner #3: Price Matching
Copy should read something like: We'll beat any price, online or anywhere else (some conditions and exclusions apply) I believe the disclaimers in parenthesis could be replaced by asterisk if it would look better.  I will link the images to the full terms.  I hope this is enough information for you.  Please feel free to take creative liberties and let me know if anything isn't working out the way I described.
I've attached image files for the products and also a screen shot of the site in case you cannot access it.

```html
<!DOCTYPE html>
<html lang="en">
<head>
<meta charset="utf-8">
<title>Velvet Orchard – Fetish Products</title>
<link rel="stylesheet" href="https://fonts.googleapis.com/css2?family=Noto+Serif:wght@400;700&family=Ubuntu:wght@400;500;700&display=swap">
<style>
  :root{
    --page:#f1f1f1;
    --white:#ffffff;
    --rule:#e2e2e2;
    --nav-text:#858585;
    --brand:#6d1534;
    --brand-red:#d2202f;
    --hero-bg:#1d1d1d;
    --hero-panel:#2a2a2a;
    --silver-light:#f2f2f2;
    --silver-dark:#a9a9a9;
    --ribbon:#c8202b;
    --ribbon-dark:#7e0f17;
    --maroon:#5a0b22;
    --maroon-dark:#3e0618;
    --promo-bg:#1a1a1a;
    --caption:#a8a8a8;
  }
  *{box-sizing:border-box;margin:0;padding:0}
  html,body{width:1200px;height:870px;overflow:hidden}
  body{background:var(--page);position:relative;font-family:"Noto Serif",Georgia,serif}
  .abs{position:absolute}

  /* header */
  .site-header{position:absolute;left:0;top:0;width:1200px;height:113px;background:var(--white);border-bottom:1px solid var(--rule)}
  .brand{position:absolute;left:458px;top:24px;width:300px;text-align:center}
  .brand-row{display:flex;align-items:center;justify-content:center;gap:12px}
  .brand-dot{width:40px;height:40px;border-radius:50%;background:var(--brand-red)}
  .brand-name{font-family:"Noto Serif",Georgia,serif;font-size:36px;font-weight:400;color:var(--brand);line-height:44px}
  .brand-tag{margin-top:22px;font-size:11px;letter-spacing:7px;color:#333;font-family:"Noto Serif",Georgia,serif}
  .cart{position:absolute;left:904px;top:26px;display:flex;align-items:center}
  .cart-label{margin-left:8px;font-size:12px;color:#222;font-family:"Noto Serif",Georgia,serif}
  .cart-caret{position:absolute;left:127px;top:19px}

  /* navigation */
  .main-nav{position:absolute;left:0;top:113px;width:1200px;height:50px;background:var(--white);box-shadow:0 3px 3px rgba(0,0,0,.05)}
  .nav-item{position:absolute;top:0;height:50px;border-left:1px solid var(--rule);border-right:1px solid var(--rule);font-size:16px;font-weight:700;color:var(--nav-text);line-height:52px;padding-left:20px}
  .nav-item svg{position:absolute;top:21px}
  .search-field{position:absolute;left:889px;top:0;width:148px;height:50px;border-left:1px solid var(--rule)}
  .search-btn{position:absolute;left:1036px;top:0;width:48px;height:50px;border-left:1px solid var(--rule);border-right:1px solid var(--rule)}

  /* hero */
  .hero-card{position:absolute;left:134px;top:195px;width:950px;height:417px;background:var(--white);box-shadow:0 0 2px rgba(0,0,0,.06)}
  .hero{position:absolute;left:141px;top:202px;width:936px;height:403px;background:radial-gradient(ellipse at 60% 40%,#2e2e2e,var(--hero-bg) 70%);overflow:hidden}
  .silver-bar{position:absolute;left:0;width:936px;height:10px;background:linear-gradient(90deg,var(--silver-dark),var(--silver-light) 30%,#c8c8c8 60%,var(--silver-light) 85%,var(--silver-dark))}
  .hero-photo{position:absolute;left:6px;top:18px;width:400px;height:370px;border-radius:40% 30% 45% 35%;background:radial-gradient(ellipse at 50% 45%,#d8d8d8,#8f8f8f 45%,rgba(30,30,30,0) 72%)}
  .hero-keys{position:absolute;left:400px;top:305px;width:110px;height:75px;background:radial-gradient(ellipse,#9a9a9a,rgba(30,30,30,0) 70%)}
  .hero-lock{position:absolute;left:842px;top:268px;width:72px;height:110px;border-radius:10px;background:radial-gradient(ellipse at 50% 65%,#b79a45,#6f5a22 60%,rgba(30,30,30,0) 80%)}
  .hero-title{position:absolute;left:380px;top:28px;width:544px;text-align:center;font-family:"Ubuntu",Arial,sans-serif;font-weight:700;font-size:46px;line-height:47px;letter-spacing:1px;color:#f4f4f4;text-shadow:0 2px 3px #000}
  .hero-rule{position:absolute;left:400px;top:142px;width:500px;height:1px;background:linear-gradient(90deg,rgba(255,255,255,0),#777 20%,#777 80%,rgba(255,255,255,0))}
  .hero-sub{position:absolute;left:380px;top:148px;width:544px;text-align:center;font-family:"Ubuntu",Arial,sans-serif;font-size:30px;color:#e8e8e8}
  .hero-note{position:absolute;width:402px;height:60px;background:var(--hero-panel);text-align:center;font-family:Arial,Helvetica,sans-serif;font-size:20px;line-height:21px;color:var(--caption);padding-top:8px}

  /* promo banners */
  .promo-card{position:absolute;top:622px;width:310px;height:201px;background:var(--white)}
  .promo{position:absolute;left:7px;top:7px;width:296px;height:187px;background:radial-gradient(ellipse at 50% 40%,#2a2a2a,var(--promo-bg) 75%);overflow:hidden;border-top:2px solid var(--maroon)}
  .promo-ribbon{position:absolute;left:16px;top:12px}
  .promo-title{position:absolute;left:0;top:13px;width:296px;text-align:center;font-size:25px;color:var(--white);line-height:32px}
  .promo-copy{position:absolute;left:0;top:70px;width:296px;text-align:center;color:#f0f0f0;text-shadow:0 1px 2px #000}
  .promo-copy .small{font-size:19px;line-height:26px}
  .promo-copy .big{font-size:24px;line-height:30px}
  .promo-copy .fine{font-family:Arial,Helvetica,sans-serif;font-size:9px;line-height:16px}
  .promo-foot{position:absolute;left:0;top:136px;width:296px;height:51px;background:linear-gradient(180deg,#1c1c1c,var(--maroon-dark) 55%,var(--maroon))}
  .promo-btn{position:absolute;left:77px;top:159px;width:144px;height:28px;background:var(--maroon);text-align:center;font-size:18px;font-weight:700;color:var(--white);line-height:29px}

  .next-card{position:absolute;left:134px;top:853px;width:950px;height:40px;background:var(--white)}
</style>
</head>
<body>

<header class="site-header">
  <div class="brand">
    <div class="brand-row">
      <span class="brand-dot"></span>
      <span class="brand-name">Velvet Orchard</span>
    </div>
    <div class="brand-tag">FETISH PRODUCTS</div>
  </div>
  <div class="cart">
    <svg width="34" height="44" viewBox="0 0 34 44" aria-hidden="true">
      <path d="M3 12 L28 8 L32 38 L6 42 Z" fill="#fafafa" stroke="#cfcfcf"/>
      <path d="M11 12 Q13 2 19 3 Q23 4 22 10" fill="none" stroke="#bbb" stroke-width="1.5"/>
    </svg>
    <span class="cart-label">EMPTY</span>
    <svg class="cart-caret" width="10" height="6" viewBox="0 0 10 6" aria-hidden="true"><path d="M0 0h10L5 6z" fill="#c8c8c8"/></svg>
  </div>
</header>

<nav class="main-nav">
  <div class="nav-item" style="left:134px;width:105px">HOME
    <svg style="left:84px" width="10" height="6" viewBox="0 0 10 6" aria-hidden="true"><path d="M0 0h10L5 6z" fill="#999"/></svg>
  </div>
  <div class="nav-item" style="left:238px;width:165px">HELP &amp; INFO
    <svg style="left:143px" width="10" height="6" viewBox="0 0 10 6" aria-hidden="true"><path d="M0 0h10L5 6z" fill="#999"/></svg>
  </div>
  <div class="search-field"></div>
  <div class="search-btn">
    <svg style="position:absolute;left:17px;top:18px" width="14" height="14" viewBox="0 0 14 14" aria-hidden="true">
      <circle cx="6" cy="6" r="4.5" fill="none" stroke="#444" stroke-width="2"/>
      <path d="M9.3 9.3L13 13" stroke="#444" stroke-width="2.2" stroke-linecap="round"/>
    </svg>
  </div>
</nav>

<section class="hero-card">
  <div class="hero" style="left:7px;top:7px">
    <div class="silver-bar" style="top:0"></div>
    <div class="silver-bar" style="top:393px"></div>
    <div class="hero-photo" role="img" aria-label="Polished steel locking plug with T-bar handle and open expanding petals"></div>
    <div class="hero-keys" role="img" aria-label="Two small silver keys"></div>
    <div class="hero-lock" role="img" aria-label="Brass padlock"></div>
    <h1 class="hero-title">MARIGOLD ALLOY<br>LOCKING ANAL PLUG</h1>
    <div class="hero-rule"></div>
    <p class="hero-sub">Add a new dimension to anal play!</p>
    <p class="hero-note" style="left:452px;top:203px">Use the lock and key to keep the<br>fully expanded plug in place.</p>
    <p class="hero-note" style="left:451px;top:280px">The bar handle allows for easy grip and<br>manipulation of plug's position.</p>
  </div>
</section>

<section class="promo-card" style="left:134px">
  <div class="promo">
    <svg class="promo-ribbon" width="264" height="36" viewBox="0 0 264 36" aria-hidden="true">
      <path d="M0 4H14L14 30H6Z" fill="var(--ribbon-dark)"/>
      <path d="M264 4H250V30H258Z" fill="var(--ribbon-dark)"/>
      <path d="M12 0H252L246 32H18Z" fill="var(--ribbon)"/>
    </svg>
    <h2 class="promo-title">RETURN POLICY</h2>
    <div class="promo-copy"><div class="small">Easy Returns, Don't like it?</div><div class="big">Send it back!</div></div>
    <div class="promo-foot"></div>
    <div class="promo-btn">LEARN MORE</div>
  </div>
</section>

<section class="promo-card" style="left:454px">
  <div class="promo">
    <svg class="promo-ribbon" width="264" height="36" viewBox="0 0 264 36" aria-hidden="true">
      <path d="M0 4H14L14 30H6Z" fill="var(--ribbon-dark)"/>
      <path d="M264 4H250V30H258Z" fill="var(--ribbon-dark)"/>
      <path d="M12 0H252L246 32H18Z" fill="var(--ribbon)"/>
    </svg>
    <h2 class="promo-title">FREE SHIPPING</h2>
    <div class="promo-copy"><div class="small">Free Expedited Shipping</div><div class="big">on orders over $149!</div></div>
    <div class="promo-foot"></div>
    <div class="promo-btn">LEARN MORE</div>
  </div>
</section>

<section class="promo-card" style="left:774px">
  <div class="promo">
    <svg class="promo-ribbon" width="264" height="36" viewBox="0 0 264 36" aria-hidden="true">
      <path d="M0 4H14L14 30H6Z" fill="var(--ribbon-dark)"/>
      <path d="M264 4H250V30H258Z" fill="var(--ribbon-dark)"/>
      <path d="M12 0H252L246 32H18Z" fill="var(--ribbon)"/>
    </svg>
    <h2 class="promo-title">PRICE MATCHING</h2>
    <div class="promo-copy" style="top:64px"><div class="small" style="font-size:20px">We'll beat any price!</div><div class="small" style="font-size:21px">Online or anywhere else.</div><div class="fine">(Some conditions and exclusions apply.)</div></div>
    <div class="promo-foot"></div>
    <div class="promo-btn">LEARN MORE</div>
  </div>
</section>

<div class="next-card"></div>

</body>
</html>
```